Business Card Design

I have a very clear idea of what I want. I just do not know how to do the graphic design to match it.

On the front I want the uploaded image with the horse and the two people.
I want

Bottom left hand corner
Lenny Firth
0472 316 508

Bottom right
There is maroon block with Morris Tane Practitioner Group Logo
Next to that I want the Stable Arc tile about the same size ( attached psd file)

On the back I want a plain colour (white) with the information

Lenny Firth
Equine Performance
Brindle4Ponies and Acupuncture
Horsemanship Lessons and Clinics
Horse Training

lfirth@critterloop.com.au
FB/lenny.firth.263
StableArc.com.au

Lenny Firth
0472 316 508
lfirth@critterloop.com.au

```html
<!DOCTYPE html>
<html lang="en">
<head>
<meta charset="utf-8">
<title>Lenny Firth – Business Card</title>
<link rel="stylesheet" href="https://fonts.googleapis.com/css2?family=Open+Sans:wght@400;600&family=Kaushan+Script&family=Cinzel:wght@500&display=swap">
<style>
  :root {
    --page-bg: #e9e7e4;
    --card-white: #ffffff;
    --ink: #1f1f1f;
    --brand-brown: #3b1f12;
    --bullet-red: #5a1a12;
    --sand-light: #cdb48a;
    --sand-mid: #b89a6c;
    --sand-dark: #8e7350;
    --silhouette: #ececec;
    --maroon: #5b2412;
    --tile-blue: #1d3f73;
  }
  * { box-sizing: border-box; margin: 0; padding: 0; }
  html, body { width: 1200px; height: 864px; overflow: hidden; }
  body {
    background: var(--page-bg);
    font-family: "Open Sans", Arial, sans-serif;
    color: var(--ink);
    position: relative;
  }
  .card {
    position: absolute;
    left: 320px;
    width: 560px;
    height: 320px;
    overflow: hidden;
    box-shadow: 0 6px 18px rgba(0,0,0,.18);
  }

  /* Back */
  .card-back { top: 80px; background: var(--card-white); }
  .back-art {
    position: absolute; left: 40px; top: 10px; width: 500px; height: 240px;
    background: radial-gradient(ellipse at 55% 45%, var(--silhouette) 0%, rgba(236,236,236,0) 70%);
  }
  .services {
    position: absolute; top: 52px; left: 0; right: 0;
    text-align: center; list-style: none;
    font-size: 16px; line-height: 20px; letter-spacing: .3px;
  }
  .services li.bullet::before { content: "• "; }
  .back-name {
    position: absolute; top: 160px; left: 0; right: 0; text-align: center;
    font-family: "Kaushan Script", cursive; font-size: 26px; line-height: 32px; color: var(--brand-brown);
  }
  .back-phone {
    position: absolute; top: 196px; left: 0; right: 0; text-align: center;
    font-size: 14px; font-weight: 600; letter-spacing: .4px;
  }
  .contacts {
    position: absolute; top: 258px; left: 30px; right: 30px;
    display: flex; justify-content: space-between; list-style: none; font-size: 12.5px;
  }
  .contacts li::before { content: "● "; color: var(--bullet-red); font-size: 8px; vertical-align: 2px; }

  /* Front */
  .card-front { top: 464px; }
  .front-photo {
    position: absolute; inset: 0;
    background: linear-gradient(170deg, var(--sand-light) 0%, var(--sand-mid) 55%, var(--sand-dark) 100%);
  }
  .headline { position: absolute; left: 0; top: 0; width: 560px; height: 320px; }
  .headline .arc-text { font-family: "Cinzel", serif; font-size: 16px; fill: var(--brand-brown); }
  .headline .script { font-family: "Kaushan Script", cursive; fill: var(--brand-brown); }
  .front-contact {
    position: absolute; left: 24px; bottom: 18px; color: var(--brand-brown);
  }
  .front-name { font-family: "Kaushan Script", cursive; font-size: 22px; line-height: 26px; }
  .front-phone { font-size: 13px; font-weight: 600; letter-spacing: .4px; }
  .partner-row {
    position: absolute; right: 22px; bottom: 18px; display: flex; gap: 10px; align-items: flex-end;
  }
  .tile {
    width: 64px; height: 64px; display: flex; align-items: center; justify-content: center;
    text-align: center; font-size: 9px; font-weight: 600; line-height: 11px; padding: 4px;
  }
  .tile-stable-arc { background: var(--card-white); color: var(--tile-blue); border-radius: 6px; }
  .tile-practitioner { background: var(--maroon); color: var(--sand-light); }
</style>
</head>
<body>

<section class="card card-back" aria-label="Card back">
  <div class="back-art" role="img" aria-label="Faint silhouette of a horse jumping"></div>
  <ul class="services">
    <li>Lenny Firth</li>
    <li class="bullet">Equine Performance</li>
    <li class="bullet">Brindle4Ponies and Acupuncture</li>
    <li class="bullet">Horsemanship Lessons and Clinics</li>
    <li class="bullet">Horse Training</li>
  </ul>
  <p class="back-name">Lenny Firth</p>
  <p class="back-phone">0472 316 508</p>
  <ul class="contacts">
    <li>lfirth@critterloop.com.au</li>
    <li>FB/lenny.firth.263</li>
    <li>StableArc.com.au</li>
  </ul>
</section>

<section class="card card-front" aria-label="Card front">
  <div class="front-photo" role="img" aria-label="Photo of a trainer watching a woman lunge a bay horse in a sandy arena"></div>
  <svg class="headline" viewBox="0 0 560 320" aria-label="How you ever gonna know your potential">
    <defs>
      <path id="headline-arc" d="M36 64 Q 200 22 360 58"/>
    </defs>
    <text class="arc-text"><textPath href="#headline-arc" textLength="318" lengthAdjust="spacing">HOW YOU EVER GONNA KNOW</textPath></text>
    <path d="M34 76 Q 200 40 372 70" fill="none" stroke="var(--brand-brown)" stroke-width="2.5" stroke-linecap="round"/>
    <text class="script" x="170" y="102" font-size="24">Your</text>
    <text class="script" x="60" y="152" font-size="58">Potential</text>
    <path d="M30 128 Q 60 150 120 160 Q 200 170 270 158" fill="none" stroke="var(--brand-brown)" stroke-width="2" stroke-linecap="round"/>
  </svg>
  <div class="front-contact">
    <p class="front-name">Lenny Firth</p>
    <p class="front-phone">0472 316 508</p>
  </div>
  <div class="partner-row">
    <div class="tile tile-stable-arc">Stable Arc</div>
    <div class="tile tile-practitioner">Morris Tane Practitioner Group</div>
  </div>
</section>

</body>
</html>
```